Denver-based business coaching & networking business needs marketing postcard design

We need help designing an oversized postcard that our sales team can use as a leave-behind when they are talking to different businesses and professionals. We have a program that has business owners and sales professionals attend a one day seminar to develop an executable business plan online that is ready to be implemented. Following the seminar they participate in bi-weekly group meetings where they collaborate with other professionals, review and stay accountable to their plan, and pass referrals. We would like to have a few graphics included from our website (www.quantelia.com) including the Spark-Shape-Unite graphic and the "Five Traps Growth Strategies Miss" graphic. The final design should be able to have a clear call-to-action about attending a seminar to begin their journey with Quantelia.

Language we would like to have included is as follows:

Learn Business Strategy
Create an Executable Business Plan
Receive Consistent Coaching
Attend Additional Educational Sessions
Profit from Peer Collaboration
Stay Accountable through Bi-Weekly Meetings
Increase your income through Referrals

The role of Quantelia is to develop successful business people through education, collaboration and community. This is created by first attending a one day seminar whose purpose is to assist attendees in creating an immediately executable business plan. Attendees then meet bi-weekly to pass referrals, collaborate on challenges and continually check in on their own plans, to ensure their continued success.

Target Market(s)

Age 28-45, Realtors, Mortgage Brokers, Insurance Professionals, Financial Advisors, CPA's, Attorneys, Small Business Owners

Industry/Entity Type

Business Consultant

Font styles to use
Sans Serif

Colors
faa54b
f37122

Requirements
Must have
• Quantelia logo, text that was provided in description, graphics that hit on elements from our website, call to action, website address

```html
<!DOCTYPE html>
<html lang="en">
<head>
<meta charset="utf-8">
<title>Quantelia Postcard</title>
<link href="https://fonts.googleapis.com/css2?family=Raleway:wght@400;500;700;800;900&display=swap" rel="stylesheet">
<style>
:root{
  --orange:#f39237;
  --orange-light:#faa54b;
  --orange-deep:#f37122;
  --ink:#3d3d3d;
  --text:#4a4a4a;
  --paper:#ffffff;
  --backdrop:#e6e6e6;
  --stamp:#eceeef;
}
*{margin:0;padding:0;box-sizing:border-box}
html,body{width:960px;height:1200px;overflow:hidden}
body{background:var(--backdrop);font-family:'Raleway',sans-serif;position:relative}
.card{position:absolute;left:66px;width:830px;background:var(--paper)}
.card-front{top:57px;height:533px;background:linear-gradient(135deg,#fbf7f2 0%,#ffffff 45%,#f6f4f2 100%)}
.card-front .accent-bar{position:absolute;left:0;right:0;bottom:0;height:10px;background:var(--orange)}
.brand{position:absolute;display:flex;align-items:center;gap:12px;font-family:'Raleway',sans-serif;font-weight:500;letter-spacing:-1px;line-height:1}
.brand-mark{display:block;background:var(--orange)}
.card-front .brand{left:292px;top:20px;color:var(--ink);font-size:50px}
.card-front .brand-mark{width:40px;height:40px}
.photo{position:absolute}
.photo-meeting{left:22px;top:101px;width:385px;height:213px;background:linear-gradient(120deg,#b88e6e 0%,#8a6446 40%,#e9e6e1 60%,#5e6f80 100%)}
.photo-laptop{left:22px;top:323px;width:185px;height:176px;background:linear-gradient(135deg,#dfe8ee 0%,#9fb4c4 60%,#e8eef2 100%)}
.photo-table{left:215px;top:323px;width:192px;height:176px;background:linear-gradient(135deg,#7a5a3e 0%,#b9a38b 50%,#4c4c52 100%)}
.intro{position:absolute;left:426px;top:101px;width:382px;font-size:13.6px;line-height:17.6px;color:var(--text);text-align:justify}
.benefits{position:absolute;left:428px;top:253px;width:390px;list-style:none}
.benefits li{position:absolute;left:0;display:flex;align-items:center;gap:13px;font-size:17px;color:var(--text);line-height:17px;width:390px}
.benefits svg{flex:none;width:30px;height:30px}
.card-back{top:612px;height:534px}
.back-panel{position:absolute;left:0;top:0;width:414px;height:534px;background:var(--orange)}
.card-back .brand{left:52px;top:28px;color:#fff;font-size:44px}
.card-back .brand-mark{width:34px;height:34px;background:#fff}
.photo-desk{left:20px;top:93px;width:374px;height:219px;background:linear-gradient(135deg,#e8e2d8 0%,#c9a77e 45%,#f2efe9 70%,#a98a66 100%)}
.headline{position:absolute;left:25px;top:336px;color:#fff;font-size:26px;font-weight:500;line-height:26px;text-transform:uppercase}
.contact-label{position:absolute;left:25px;top:402px;color:#fff;font-size:26px;font-weight:900}
.phone{position:absolute;left:22px;top:422px;color:#fff;font-size:52px;font-weight:900;letter-spacing:-1px}
.site{position:absolute;left:25px;top:494px;color:#fff;font-size:27px;font-weight:500}
.stamp-box{position:absolute;left:714px;top:24px;width:92px;height:90px;background:var(--stamp)}
</style>
</head>
<body>
<section class="card card-front">
  <div class="brand"><span class="brand-mark"></span>QUANTELIA</div>
  <div class="photo photo-meeting" role="img" aria-label="Photo of a team meeting around a whiteboard"></div>
  <div class="photo photo-laptop" role="img" aria-label="Photo of hands working on a laptop"></div>
  <div class="photo photo-table" role="img" aria-label="Photo of professionals at a networking table"></div>
  <p class="intro">The role of Quantelia is to develop successful business people through education, collaboration and community. This is created by first attending a one day seminar whose purpose is to assist attendees in creating an immediately executable business plan. Attendees then meet bi-weekly to pass referrals, collaborate on challenges and continually check in on their own plans, to ensure their continued success.</p>
  <ul class="benefits">
    <li style="top:0"><svg viewBox="0 0 30 30"><circle cx="15" cy="15" r="15" fill="var(--orange)"/><path d="M9 15l4 4 8-8" stroke="#fff" stroke-width="2.5" fill="none"/></svg>Learn Business Strategy</li>
    <li style="top:36px"><svg viewBox="0 0 30 30"><circle cx="15" cy="15" r="15" fill="var(--orange)"/><path d="M9 15l4 4 8-8" stroke="#fff" stroke-width="2.5" fill="none"/></svg>Create an Executable Business Plan</li>
    <li style="top:70px"><svg viewBox="0 0 30 30"><circle cx="15" cy="15" r="15" fill="var(--orange)"/><path d="M9 15l4 4 8-8" stroke="#fff" stroke-width="2.5" fill="none"/></svg>Receive Consistent Coaching</li>
    <li style="top:106px"><svg viewBox="0 0 30 30"><circle cx="15" cy="15" r="15" fill="var(--orange)"/><path d="M9 15l4 4 8-8" stroke="#fff" stroke-width="2.5" fill="none"/></svg>Attend Additional Educational Sessions</li>
    <li style="top:141px"><svg viewBox="0 0 30 30"><circle cx="15" cy="15" r="15" fill="var(--orange)"/><path d="M9 15l4 4 8-8" stroke="#fff" stroke-width="2.5" fill="none"/></svg>Profit from Peer Collaboration</li>
    <li style="top:176px"><svg viewBox="0 0 30 30"><circle cx="15" cy="15" r="15" fill="var(--orange)"/><path d="M9 15l4 4 8-8" stroke="#fff" stroke-width="2.5" fill="none"/></svg><span>Stay Accountable through Bi-Weekly<br>Meetings</span></li>
    <li style="top:214px"><svg viewBox="0 0 30 30"><circle cx="15" cy="15" r="15" fill="var(--orange)"/><path d="M9 15l4 4 8-8" stroke="#fff" stroke-width="2.5" fill="none"/></svg>Increase your income through Referrals</li>
  </ul>
  <div class="accent-bar"></div>
</section>

<section class="card card-back">
  <div class="back-panel">
    <div class="brand"><span class="brand-mark"></span>QUANTELIA</div>
    <div class="photo photo-desk" role="img" aria-label="Photo of hands reviewing charts and reports on a desk"></div>
    <h2 class="headline">Ready to build a better<br>business?</h2>
    <p class="contact-label">CONTACT US</p>
    <p class="phone">555-012-3478</p>
    <p class="site">WWW.QUANTELIA.COM</p>
  </div>
  <div class="stamp-box"></div>
</section>
</body>
</html>
```